New York Property Management Company needs a Brochure Designed

We need a brochure for a new property management company in New York called KT7 Realty Partners. The 2 is superscript (squared.) We are looking for buildings to manage and want to showcase our expertise and caring. Logo is attached. We are getting a different photo and do not need all the verbiage. Also, does not need to be a trifold.
Updates

Property management group is a RESIDENTIAL property management group. I neglected to mention that. Thanks.

Hi designers, We've received very few designs so far so we've extended the deadline. We're hoping to receive your creative submissions soon! Thank you!

Reason: A few people have to weigh in on the design and it has been difficult coordinating this. We are getting close to making a decision and just need a few more days.

Industry/Entity Type

Property Management

```html
<!DOCTYPE html>
<html lang="en">
<head>
<meta charset="UTF-8">
<title>About Us – KT7 Realty Partners</title>
<link href="https://fonts.googleapis.com/css2?family=Montserrat:wght@800&family=Questrial&display=swap" rel="stylesheet">
<style>
  :root {
    --header-brown: #3b312f;
    --panel-top: #4a4a4a;
    --panel-bottom: #666666;
    --text-light: #ffffff;
    --rule: #e9e9e9;
    --badge-bg: #5d5d5d;
    --badge-border: #8a8a8a;
    --photo-dark: #1d2f38;
    --photo-mid: #3f7f8c;
    --photo-light: #9cc4cc;
  }
  html, body {
    margin: 0;
    padding: 0;
    width: 1200px;
    height: 600px;
    overflow: hidden;
    background: #ffffff;
  }
  .brochure-page {
    position: relative;
    width: 1200px;
    height: 600px;
    overflow: hidden;
    font-family: "Questrial", "Century Gothic", sans-serif;
    color: var(--text-light);
  }
  .content-panel {
    position: absolute;
    left: 0;
    top: 0;
    width: 601px;
    height: 600px;
    background: linear-gradient(180deg, var(--panel-top) 0%, var(--panel-bottom) 100%);
  }
  .section-header {
    position: absolute;
    left: 0;
    top: 0;
    width: 601px;
    height: 89px;
    background: var(--header-brown);
    border-bottom: 3px solid var(--rule);
  }
  .section-title {
    position: absolute;
    left: 26px;
    top: 20px;
    margin: 0;
    font-family: "Montserrat", "Arial Black", sans-serif;
    font-weight: 800;
    font-size: 35px;
    letter-spacing: 0.5px;
    line-height: 1;
  }
  .brand-badge {
    position: absolute;
    left: 513px;
    top: 0;
    width: 88px;
    height: 86px;
    box-sizing: border-box;
    background: var(--badge-bg);
    border: 1px solid var(--badge-border);
    display: flex;
    align-items: center;
    justify-content: center;
    text-align: center;
  }
  .brand-name {
    font-family: "Questrial", "Century Gothic", sans-serif;
    font-size: 13px;
    line-height: 1.25;
    color: var(--text-light);
    letter-spacing: 0.5px;
  }
  .about-copy {
    position: absolute;
    left: 39px;
    top: 113px;
    width: 520px;
    font-size: 13.6px;
    line-height: 17px;
  }
  .about-intro {
    margin: 0 0 42px 0;
  }
  .value-list {
    list-style: none;
    margin: 0;
    padding: 0;
  }
  .value-item {
    margin: 0 0 17px 0;
  }
  .value-item::before {
    content: "•";
    display: inline-block;
    width: 37px;
  }
  .building-photo {
    position: absolute;
    left: 601px;
    top: 0;
    width: 599px;
    height: 600px;
    background:
      linear-gradient(100deg, transparent 0%, transparent 48%, rgba(20,40,48,0.55) 49%, rgba(40,100,112,0.35) 100%),
      linear-gradient(180deg, var(--photo-light) 0%, var(--photo-mid) 45%, var(--photo-dark) 100%);
  }
</style>
</head>
<body>
  <main class="brochure-page">
    <section class="content-panel">
      <header class="section-header">
        <h1 class="section-title">ABOUT US</h1>
        <div class="brand-badge">
          <span class="brand-name">KT7 Realty<br>Partners</span>
        </div>
      </header>

      <div class="about-copy">
        <p class="about-intro">Every cooperative, condominium and rental building has a structure and physical plant that needs ongoing attention from ownership, management, staff and outside professionals. &nbsp;In order for building operations and projects to flow smoothly, these components must work collaboratively. Management is the centerpiece of this equation. &nbsp;KT7RP provides bespoke management solutions to all buildings in its portfolio.</p>

        <ul class="value-list">
          <li class="value-item">Shareholders, unit owners and tenants are all individuals who have a home that needs the appropriate level of management to ensure a quiet, safe and well-maintained environment.</li>
          <li class="value-item">We manage multifamily dwellings the way they should be managed watching costs, providing quality service, creating value. We create value for building resulting in increased apartment/building values.</li>
          <li class="value-item">We leverage knowledge of real estate ownership, management and development to maximize appreciation and income</li>
          <li class="value-item">We believe that quality management equals integrity, accountability, ownership, reliability and responsibility.</li>
          <li class="value-item">We attract top-notch managers by providing ownership opportunities and income generating potential.</li>
        </ul>
      </div>
    </section>

    <div class="building-photo" role="img" aria-label="Photograph looking up at glass skyscrapers against the sky, in teal and slate tones"></div>
  </main>
</body>
</html>
```